Hip-Hop Artist RT Marble new album cover design for "Quiet Engines"

Artist: RT Marble
Album Title: Quiet Engines
I am attaching a un-edited picture to use & some sample images with the "Quiet Engines" concept directions. I am hoping that the graphic designers accepting this challenge can do a better or different job than the 3 sample design images attached. I do like each of the 3 attached drafts(Draft, Draft2, Draft3) concepts. But, would like to see other creative design approaches and other possible affect. artwork ideas.
I am also attaching a number of random design that I also like the direction on.
Please let em know if you have any questions, and I will respond as quickly as possible.

```html
<!DOCTYPE html>
<html lang="en">
<head>
<meta charset="utf-8">
<title>RT Marble – Quiet Engines</title>
<link rel="stylesheet" href="https://fonts.googleapis.com/css2?family=Amatic+SC:wght@400&family=Patrick+Hand+SC&display=swap">
<style>
  :root {
    --bg-deep: #1a0b0b;
    --bg-maroon: #3a1716;
    --skin-warm: #b0665a;
    --skin-light: #d99a8a;
    --skin-shadow: #5e2a25;
    --ink: #f4f1ef;
    --rule: #9a9494;
  }
  html, body {
    margin: 0;
    padding: 0;
    width: 1200px;
    height: 1108px;
    overflow: hidden;
    background: var(--bg-deep);
  }
  .cover {
    position: relative;
    width: 1200px;
    height: 1108px;
    overflow: hidden;
    background: var(--bg-deep);
  }
  .cover-photo {
    position: absolute;
    inset: 0;
    background:
      radial-gradient(ellipse 420px 620px at 1000px 560px, var(--skin-light) 0%, var(--skin-warm) 40%, rgba(94,42,37,0.6) 75%, transparent 100%),
      radial-gradient(ellipse 300px 520px at 560px 640px, rgba(140,70,60,0.85) 0%, rgba(94,42,37,0.5) 60%, transparent 100%),
      radial-gradient(ellipse 260px 480px at 200px 620px, rgba(90,40,36,0.7) 0%, transparent 100%),
      linear-gradient(180deg, var(--bg-maroon) 0%, var(--bg-deep) 100%);
  }
  .album-title {
    position: absolute;
    left: 0;
    top: 0;
    width: 1200px;
    height: 760px;
  }
  .album-title text {
    font-family: "Amatic SC", "Arial Narrow", sans-serif;
    font-weight: 400;
    font-size: 416px;
    fill: var(--ink);
  }
  .artist-bar {
    position: absolute;
    left: 0;
    top: 1036px;
    width: 1200px;
    height: 48px;
  }
  .artist-bar .rule {
    position: absolute;
    height: 8px;
    background: var(--rule);
  }
  .artist-bar .rule-left { left: 0; width: 430px; top: 18px; }
  .artist-bar .rule-right { left: 758px; width: 442px; top: 24px; }
  .artist-name {
    position: absolute;
    left: 430px;
    width: 328px;
    top: 0;
    margin: 0;
    text-align: center;
    font-family: "Patrick Hand SC", "Comic Sans MS", cursive;
    font-size: 48px;
    line-height: 48px;
    letter-spacing: 3px;
    color: var(--ink);
    font-weight: 400;
  }
</style>
</head>
<body>
  <main class="cover">
    <div class="cover-photo" role="img" aria-label="Portrait photograph of the artist shown three times, overlapping in warm red light against a dark background"></div>

    <svg class="album-title" viewBox="0 0 1200 760" aria-labelledby="album-title-text">
      <title id="album-title-text">Quiet Engines</title>
      <text x="66" y="360" textLength="510" lengthAdjust="spacingAndGlyphs">QUIET</text>
      <text x="66" y="720" textLength="698" lengthAdjust="spacingAndGlyphs">ENGINES</text>
    </svg>

    <div class="artist-bar">
      <span class="rule rule-left"></span>
      <h1 class="artist-name">RT Marble</h1>
      <span class="rule rule-right"></span>
    </div>
  </main>
</body>
</html>
```